Maple Hollow Skilled Nursing Facility

We are a skilled nursing facility that cares for elderly when they have come from the hospital and are trying to transition to make it back to their homes! We strive to create an environment that is friendly with great service to meet their needs and take care of them. The task is to create a website that informs the community of our excellent service and care. I will upload our logo and a brochure to give some ideas.
Target Market(s)
Families who will be looking at care facilities and rating them based on their quality for their loved ones.
Coding
Coded - Design and coding required
Number of Pages Required
5+ page
Requirements
Must have
- Social Media Integration.
Nice to have
- Nice, professional and clean. A warming website that is inviting to those who see.

```html
<!DOCTYPE html>
<html lang="en">
<head>
<meta charset="utf-8">
<title>Maple Hollow Skilled Nursing Facility</title>
<link href="https://fonts.googleapis.com/css2?family=Cinzel:wght@400;700&family=Lato:wght@400;700&family=Ubuntu:wght@500&display=swap" rel="stylesheet">
<style>
:root{
  --green:#43a10a;
  --blue:#0466c8;
  --orange:#ff6a00;
  --ink:#222;
  --grey-bg:#e8e8e8;
  --footer:#1c1c1c;
  --white:#fff;
}
*{box-sizing:border-box;margin:0;padding:0}
html,body{width:1200px;height:1103px;overflow:hidden}
body{position:relative;font-family:'Lato',sans-serif;color:var(--ink);background:var(--white)}
.hero{position:absolute;left:0;top:0;width:1200px;height:727px;
  background:linear-gradient(180deg,#f4f7fb 0%,#e9eef5 40%,#cfd5dc 75%,#8c9197 100%)}
.hero-photo{position:absolute;left:560px;top:240px;width:640px;height:487px;
  background:radial-gradient(ellipse at 60% 45%,#c9d8ea 0%,#a9bfd6 35%,rgba(170,190,210,0) 72%)}
.call{position:absolute;left:77px;top:20px;display:flex;align-items:center;gap:9px}
.call-icon{width:36px;height:36px;border:1px solid #888;border-radius:50%;background:#fff;display:flex;align-items:center;justify-content:center}
.call-label{font-family:'Cinzel',serif;font-size:14px;color:#333;letter-spacing:.5px}
.call-number{font-family:'Cinzel',serif;font-size:24px;color:var(--green);margin-left:2px}
.social{position:absolute;left:941px;top:20px;display:flex;align-items:center;gap:8px}
.social .divider{width:1px;height:22px;background:#bbb;margin-right:12px}
.social .dot{width:31px;height:31px;border-radius:50%;background:#3b7fc2}
.nav{position:absolute;left:82px;top:75px;width:1036px;height:44px}
.nav-bar{position:absolute;inset:0}
.nav a{position:absolute;top:0;height:44px;line-height:44px;font-family:Arial,sans-serif;font-weight:700;font-size:13px;color:var(--white);text-decoration:none}
.nav a.active{top:7px;height:29px;line-height:29px;width:89px;left:5px;text-align:center;background:linear-gradient(#fff,#e4e4e4);color:var(--green);border-radius:2px}
.nav .sep{position:absolute;top:12px;width:1px;height:22px;background:rgba(255,255,255,.35)}
.brand{position:absolute;left:500px;top:10px;width:200px;text-align:center}
.brand-mark{width:52px;height:52px;border-radius:50%;background:var(--green);margin:0 auto 14px}
.brand-name{font-family:'Cinzel',serif;font-weight:700;font-size:17px;color:#1d2a3a;line-height:1}
.brand-sub{font-family:'Cinzel',serif;font-weight:700;font-size:17px;color:#1d2a3a;margin-top:2px}
.slide-arrow{position:absolute;top:320px;width:53px;height:53px;border-radius:50%;background:rgba(200,205,210,.75);display:flex;align-items:center;justify-content:center}
.slide-arrow.prev{left:12px}
.slide-arrow.next{left:1135px;width:45px;height:45px;top:324px}
.headline{position:absolute;left:136px;top:290px;font-family:'Cinzel',serif;font-weight:700}
.headline .l1{font-size:36px;color:#111;line-height:42px}
.headline .l2{font-size:48px;color:var(--orange);line-height:56px}
.card{position:absolute;top:566px;width:329px;height:124px;background:rgba(255,255,255,.95);box-shadow:0 4px 10px rgba(0,0,0,.25);overflow:hidden}
.card .corner{position:absolute;left:0;top:0}
.card h3{position:absolute;top:15px;font-family:'Ubuntu',sans-serif;font-weight:500;font-size:19px;color:#222;letter-spacing:.5px}
.card p{position:absolute;top:42px;width:230px;font-size:14px;line-height:21.5px;color:#333}
.card .more{position:absolute;right:0;bottom:0}
.lower{position:absolute;left:0;top:727px;width:1200px;height:332px;background:var(--grey-bg)}
.lower svg.split{position:absolute;left:0;top:0}
.about{position:absolute;left:82px;top:37px;width:512px;color:var(--white)}
.about h2,.inquiry h2{font-family:'Cinzel',serif;font-weight:400;font-size:31px;letter-spacing:.5px}
.rule{position:relative;height:1px;margin-top:10px}
.about .rule{background:rgba(255,255,255,.8);width:514px;margin-left:-2px}
.rule::before{content:"";position:absolute;left:0;top:-1px;width:52px;height:2px}
.about .rule::before{background:#0c2f5c}
.about p{margin-top:20px;font-size:15px;line-height:25.6px;width:520px}
.btn{display:inline-block;background:var(--orange);color:var(--white);font-weight:700;font-size:14.5px;text-align:center;border:none}
.about .btn{margin-top:20px;width:106px;height:32px;line-height:32px}
.inquiry{position:absolute;left:744px;top:32px;width:371px}
.inquiry h2{color:#111}
.inquiry h2 span{color:var(--blue)}
.inquiry .rule{background:#bbb;margin-top:6px}
.inquiry .rule::before{background:#111;width:52px}
.field{position:absolute;background:var(--white);border:1px solid #bbb;font-size:13px;color:#555;padding:9px 8px}
.inquiry .btn{position:absolute;left:5px;top:233px;width:106px;height:31px;line-height:31px}
.footer{position:absolute;left:0;top:1059px;width:1200px;height:44px;background:var(--footer);color:#e6e6e6;font-size:13px;text-align:center;line-height:44px}
</style>
</head>
<body>

<section class="hero">
  <div class="hero-photo" role="img" aria-label="Photo of a smiling senior woman in a wheelchair with a caregiver in a bright living room"></div>

  <div class="call">
    <span class="call-icon"><svg width="16" height="16" viewBox="0 0 24 24"><path d="M6.6 10.8a15 15 0 0 0 6.6 6.6l2.2-2.2c.3-.3.7-.4 1-.2 1.1.4 2.3.6 3.6.6.6 0 1 .4 1 1V20c0 .6-.4 1-1 1A17 17 0 0 1 3 4c0-.6.4-1 1-1h3.5c.6 0 1 .4 1 1 0 1.3.2 2.5.6 3.6.1.3 0 .7-.2 1z" fill="#222"/></svg></span>
    <span class="call-label">Call us now :</span>
    <span class="call-number">(555) 214-7730</span>
  </div>

  <div class="social" aria-label="Social media links">
    <span class="divider"></span>
    <span class="dot" aria-label="Social link 1"></span>
    <span class="dot" aria-label="Social link 2"></span>
    <span class="dot" aria-label="Social link 3"></span>
    <span class="dot" aria-label="Social link 4"></span>
  </div>

  <nav class="nav">
    <svg class="nav-bar" width="1036" height="44" viewBox="0 0 1036 44">
      <path d="M0 0H418L405 44H0Z" fill="var(--green)"/>
      <path d="M610 0H1036V44H623Z" fill="var(--green)"/>
      <path d="M418 0L424 -30L410 44H405Z" fill="#d8d8d8"/>
      <path d="M610 0L604 -30L618 44H623Z" fill="#d8d8d8"/>
    </svg>
    <a class="active" href="#">Home</a>
    <a href="#" style="left:123px">About Us</a>
    <span class="sep" style="left:245px"></span>
    <a href="#" style="left:307px">Services</a>
    <a href="#" style="left:645px">therapy &amp; Rehab</a>
    <span class="sep" style="left:776px"></span>
    <a href="#" style="left:804px">Testimonials</a>
    <span class="sep" style="left:912px"></span>
    <a href="#" style="left:940px">Contact Us</a>
  </nav>

  <div class="brand">
    <div class="brand-mark"></div>
    <div class="brand-name">Maple Hollow</div>
    <div class="brand-sub">Post Acute</div>
  </div>

  <span class="slide-arrow prev"><svg width="20" height="34" viewBox="0 0 20 34"><path d="M17 2L3 17l14 15" stroke="#fff" stroke-width="2" fill="none"/></svg></span>
  <span class="slide-arrow next"><svg width="16" height="30" viewBox="0 0 16 30"><path d="M3 2l11 13L3 28" stroke="#fff" stroke-width="2" fill="none"/></svg></span>

  <h1 class="headline"><div class="l1">Your Care.</div><div class="l2">Our Passion.</div></h1>

  <article class="card" style="left:80px">
    <svg class="corner" width="60" height="84"><path d="M0 0H60Q40 70 0 84Z" fill="var(--blue)"/></svg>
    <h3 style="left:74px">Nursing Services</h3>
    <p style="left:74px">Lorem ipsum dolor consectetn mr adipiscing elit. Cras nibh efficitl utv nibh in accumsan hen</p>
    <svg class="more" width="36" height="36"><path d="M36 0V36H0Z" fill="#666"/><path d="M26 19v12M20 25h12" stroke="#fff" stroke-width="1.6"/></svg>
  </article>
  <article class="card" style="left:433px">
    <svg class="corner" width="72" height="84"><path d="M0 0H72Q50 70 0 84Z" fill="var(--green)"/></svg>
    <h3 style="left:85px">Rehabilitation</h3>
    <p style="left:85px">Lorem ipsum dolor consectetn mr adipiscing elit. Cras nibh efficitl utv nibh in accumsan hen</p>
    <svg class="more" width="36" height="36"><path d="M36 0V36H0Z" fill="#666"/><path d="M26 19v12M20 25h12" stroke="#fff" stroke-width="1.6"/></svg>
  </article>
  <article class="card" style="left:786px">
    <svg class="corner" width="68" height="84"><path d="M0 0H68Q46 70 0 84Z" fill="var(--orange)"/></svg>
    <h3 style="left:81px">Therepy Services</h3>
    <p style="left:81px">Lorem ipsum dolor consectetn mr adipiscing elit. Cras nibh efficitl utv nibh in accumsan hen</p>
    <svg class="more" width="36" height="36"><path d="M36 0V36H0Z" fill="#666"/><path d="M26 19v12M20 25h12" stroke="#fff" stroke-width="1.6"/></svg>
  </article>
</section>

<section class="lower">
  <svg class="split" width="1200" height="332" viewBox="0 0 1200 332">
    <path d="M0 0H700L617 332H0Z" fill="var(--blue)"/>
    <path d="M706 0H713L629 332H622Z" fill="var(--blue)"/>
  </svg>

  <div class="about">
    <h2>About Us</h2>
    <div class="rule"></div>
    <p>Lorem ipsum dolor sit amet, consectetuer adipiscing elit, sed diam nonummy nibh euismod tincidunt ut laoreet dolore magna aliquam erat volutpat. Ut wisi enim ad minim veniam, quis nostrud exerci tation ullamcorper suscipit lobortis nisl ut aliquip ex ea commodo consequat. Duis autem vel eum iriure dolor in hendrerit in vulputate velit esse molestie consequat, vel illum dolore eu feugiat nulla facilisis at vero eros et accumsan et iusto</p>
    <a class="btn" href="#">READ MORE</a>
  </div>

  <form class="inquiry">
    <h2>Quick <span>Inquiry</span></h2>
    <div class="rule"></div>
    <div class="field" style="left:4px;top:77px;width:178px;height:33px">Name</div>
    <div class="field" style="left:193px;top:77px;width:178px;height:33px">Phone</div>
    <div class="field" style="left:4px;top:120px;width:367px;height:33px">Email</div>
    <div class="field" style="left:4px;top:163px;width:367px;height:52px">Message</div>
    <button class="btn" type="button">SUBMIT</button>
  </form>
</section>

<footer class="footer">© 2016 Maple Hollow Care. | All Rights Reserved</footer>

</body>
</html>
```